Progressive Architecture and Urban Planning Studio - Stationery Design

The Kestrel Collective: a small boutique Architectural and Urban Planning Studio based in Natal/ RN, Brazil, about to open branches in South Africa and West Africa, established to provide high quality, innovative design and personal client service for projects worldwide. Our approach to Architecture: Minimal - Less is More, so to speak, but with an edge! Strive to produce "clean" projects - stripped of all that can be stripped, no excesses. Got our Logo right here with Pixel Harbor, and hope to do the same with our stationery (were informed that includes business cards, letterhead and envelopes). Since we'll be using two clour schemes, we want at least one using a black background (business card). We'll also allow manipulation of our logo if it helps the final design. Good Luck!

Font styles to use
Other font styles liked:
• Nexa

Colors

Designer to choose colors to be used in the design.

Requirements
Must have
• Business Cards/ Letterheads with the following address:
Rua Olavo Pereira 2741, Vale Dourado, Natal/RN
Should be able to edit it.

```html
<!DOCTYPE html>
<html lang="en">
<head>
<meta charset="utf-8">
<title>The Kestrel Collective – Business Card</title>
<link rel="stylesheet" href="https://fonts.googleapis.com/css2?family=Montserrat:wght@400&family=Nothing+You+Could+Do&family=Source+Sans+3:wght@400;600&display=swap">
<style>
  :root {
    --backdrop: #dde2e3;
    --card: #050505;
    --ink: #f2f2f2;
    --ink-soft: #cfcfcf;
    --accent: #c4122f;
    --facet-light: #e4e4e4;
    --facet-mid: #bdbdbd;
  }
  * { margin: 0; padding: 0; box-sizing: border-box; }
  html, body {
    width: 1200px;
    height: 848px;
    overflow: hidden;
    background: var(--backdrop);
  }
  .canvas {
    position: relative;
    width: 1200px;
    height: 848px;
  }
  .card {
    position: absolute;
    width: 520px;
    height: 300px;
    background: var(--card);
    box-shadow: 0 14px 30px rgba(0, 0, 0, 0.25);
    color: var(--ink);
  }
  .card--front { left: 70px; top: 430px; }
  .card--back  { left: 610px; top: 130px; }

  .brand-name {
    position: absolute;
    font-family: "Montserrat", sans-serif;
    font-weight: 400;
    font-size: 13px;
    letter-spacing: 0.42em;
    text-transform: uppercase;
    color: var(--ink);
    white-space: nowrap;
  }
  .card--front .brand-name { right: 34px; top: 38px; }
  .card--back .brand-name  { right: 30px; top: 34px; }

  .holder {
    position: absolute;
    left: 90px;
    top: 96px;
  }
  .holder__name {
    font-family: "Nothing You Could Do", cursive;
    font-size: 48px;
    line-height: 1;
    color: var(--ink);
  }
  .holder__role {
    font-family: "Source Sans 3", sans-serif;
    font-size: 17px;
    color: var(--ink);
    text-align: right;
    margin-top: -2px;
    padding-right: 4px;
  }

  .contact {
    position: absolute;
    left: 90px;
    bottom: 40px;
    font-family: "Source Sans 3", sans-serif;
    font-size: 15px;
    line-height: 1.35;
    color: var(--ink-soft);
  }
  .contact__label {
    font-weight: 600;
    color: var(--accent);
    margin-right: 2px;
  }
  .contact__label--fax { margin-left: 8px; }

  .facet-graphic {
    position: absolute;
    left: 30px;
    top: 80px;
    width: 470px;
    height: 190px;
  }
</style>
</head>
<body>
<main class="canvas">

  <section class="card card--front" aria-label="Business card, front">
    <p class="brand-name">The Kestrel Collective</p>
    <div class="holder">
      <p class="holder__name">Project Owner</p>
      <p class="holder__role">director</p>
    </div>
    <address class="contact">
      <span class="contact__line">Rua Olavo Pereira 2741, Vale Dourado, Natal/RN</span><br>
      <span class="contact__label">T</span>00 000 0000
      <span class="contact__label contact__label--fax">F</span>00 000 0000
    </address>
  </section>

  <section class="card card--back" aria-label="Business card, back">
    <p class="brand-name">The Kestrel Collective</p>
    <svg class="facet-graphic" viewBox="0 0 470 190" role="img" aria-label="Abstract light grey architectural facet artwork fanning out from left to right">
      <defs>
        <linearGradient id="facetTone" x1="0" y1="1" x2="1" y2="0">
          <stop offset="0" stop-color="var(--facet-mid)"/>
          <stop offset="1" stop-color="var(--facet-light)"/>
        </linearGradient>
      </defs>
      <rect x="0" y="0" width="470" height="190" fill="url(#facetTone)" opacity="0.85"/>
    </svg>
  </section>

</main>
</body>
</html>
```